Bref créative
vostelmira #20
Real Estate Investors
Professional
Dale Quistorff
President
8316 Willowmere Rd, Ste. 217 (#492)
Frisco, TX 75034
dquistorff@mailvessa.com
Please make 100 cards in the name of Dale Quistorff and the other 100 cards in the name of: Colette Quistorff, Title: Program Director, Address: Same, Phone: Same, Cell: 214 637-2940, E-mail: colette.quistorff@mailvessa.com.
Keep in mind we will request an update on this card in a later date with the following: Website Address, Fax #, and Toll Free #.

```html
<!DOCTYPE html>
<html lang="en">
<head>
<meta charset="UTF-8">
<title>Tolvanex Business Card</title>
<link rel="stylesheet" href="https://fonts.googleapis.com/css2?family=Cinzel:wght@400;600&family=Open+Sans:wght@400;600&display=swap">
<style>
  :root {
    --backdrop: #e9e6e2;
    --card-black: #0d0d0d;
    --card-red: #e8323a;
    --card-red-dark: #b81f27;
    --swoosh-light: #d9d9d9;
    --swoosh-dark: #5a5a5a;
    --brand-red: #e8323a;
    --tag-grey: #9a9a9a;
    --ink-white: #ffffff;
  }
  * { box-sizing: border-box; margin: 0; padding: 0; }
  html, body {
    width: 1200px; height: 629px; overflow: hidden;
    background: var(--backdrop);
  }
  .canvas {
    position: relative; width: 1200px; height: 629px;
    display: flex; align-items: center; justify-content: center;
  }
  .card {
    position: relative; width: 980px; height: 560px;
    background: var(--card-black);
    overflow: hidden;
    box-shadow: 0 6px 18px rgba(0,0,0,0.18);
  }
  .card-shape { position: absolute; inset: 0; }
  .brand {
    position: absolute; top: 120px; left: 0; width: 100%;
    text-align: center;
  }
  .brand-name {
    font-family: "Cinzel", serif; font-weight: 600;
    font-size: 78px; letter-spacing: 3px;
    color: var(--brand-red); line-height: 1;
  }
  .brand-tagline {
    margin-top: 10px;
    font-family: "Open Sans", sans-serif; font-weight: 600;
    font-size: 15px; letter-spacing: 9px; text-transform: uppercase;
    color: var(--tag-grey);
  }
  .holder {
    position: absolute; left: 150px; top: 430px; width: 300px;
    text-align: right; color: var(--ink-white);
  }
  .holder-name {
    font-family: "Cinzel", serif; font-weight: 600; font-size: 28px;
  }
  .holder-title {
    margin-top: 4px;
    font-family: "Open Sans", sans-serif; font-size: 15px; letter-spacing: 2px;
    text-transform: uppercase;
  }
  .divider {
    position: absolute; left: 478px; top: 395px; width: 2px; height: 140px;
    background: var(--ink-white);
  }
  .contacts {
    position: absolute; left: 500px; top: 398px; list-style: none;
    font-family: "Open Sans", sans-serif; font-size: 16px; color: var(--ink-white);
  }
  .contact-line {
    display: flex; align-items: center; gap: 10px; height: 33px;
  }
  .contact-icon { width: 20px; height: 20px; flex: none; }
</style>
</head>
<body>
<main class="canvas">
  <article class="card">
    <svg class="card-shape" viewBox="0 0 980 560" width="980" height="560" aria-hidden="true">
      <defs>
        <linearGradient id="swooshTone" x1="0" y1="0" x2="1" y2="0">
          <stop offset="0" stop-color="var(--swoosh-dark)"/>
          <stop offset="0.5" stop-color="var(--swoosh-light)"/>
          <stop offset="1" stop-color="var(--swoosh-dark)"/>
        </linearGradient>
        <linearGradient id="redTone" x1="0" y1="0" x2="0" y2="1">
          <stop offset="0" stop-color="var(--card-red)"/>
          <stop offset="1" stop-color="var(--card-red-dark)"/>
        </linearGradient>
      </defs>
      <path d="M0,318 C300,418 650,398 980,292 L980,330 C650,425 300,440 0,345 Z" fill="url(#swooshTone)"/>
      <path d="M0,345 C300,440 650,425 980,330 L980,560 L0,560 Z" fill="url(#redTone)"/>
    </svg>

    <header class="brand">
      <div class="brand-name">TOLVANEX</div>
      <div class="brand-tagline">Real Estate Investors</div>
    </header>

    <div class="holder">
      <div class="holder-name">Dale Quistorff</div>
      <div class="holder-title">President</div>
    </div>

    <div class="divider"></div>

    <ul class="contacts">
      <li class="contact-line">
        <svg class="contact-icon" viewBox="0 0 20 20" aria-hidden="true"><circle cx="10" cy="10" r="10" fill="#fff"/><path d="M10 4.5a3.5 3.5 0 0 0-3.5 3.5c0 2.6 3.5 7 3.5 7s3.5-4.4 3.5-7A3.5 3.5 0 0 0 10 4.5zm0 4.8a1.3 1.3 0 1 1 0-2.6 1.3 1.3 0 0 1 0 2.6z" fill="var(--card-red)"/></svg>
        <span>8316 Willowmere Rd, Ste. 217 (#492), Frisco, TX 75034</span>
      </li>
      <li class="contact-line">
        <svg class="contact-icon" viewBox="0 0 20 20" aria-hidden="true"><circle cx="10" cy="10" r="10" fill="#fff"/><path d="M6.5 5h2l1 2.5-1.3 1a6 6 0 0 0 2.8 2.8l1-1.3 2.5 1v2a1 1 0 0 1-1 1A8.5 8.5 0 0 1 5.5 6a1 1 0 0 1 1-1z" fill="var(--card-red)"/></svg>
        <span>Office 214 637-2915</span>
      </li>
      <li class="contact-line">
        <svg class="contact-icon" viewBox="0 0 20 20" aria-hidden="true"><circle cx="10" cy="10" r="10" fill="#fff"/><rect x="7" y="4.5" width="6" height="11" rx="1.2" fill="var(--card-red)"/><rect x="8" y="6" width="4" height="7" fill="#fff"/></svg>
        <span>Cell 214 637-2940</span>
      </li>
      <li class="contact-line">
        <svg class="contact-icon" viewBox="0 0 20 20" aria-hidden="true"><circle cx="10" cy="10" r="10" fill="#fff"/><rect x="5" y="6.5" width="10" height="7" rx="1" fill="var(--card-red)"/><path d="M5.5 7l4.5 3.5L14.5 7" stroke="#fff" stroke-width="1" fill="none"/></svg>
        <span>dquistorff@mailvessa.com</span>
      </li>
    </ul>
  </article>
</main>
</body>
</html>
```